Upsell Vertical Banner Ad Design For B2B Marketing Agency Vertical 768px × 1180px IS THE SIZE

I need a banner made for my website www.brightharborgrowthworks.biz This banner will be an upsell advertisement for after someone signs up for my monthly program. When they login to their account for the 1st time I will give them the chance to upgrade their account to our annual program with just one click.

this is a page that upsells it currently to give you an idea how we market ourselves:
https://bhgw.pagevault-example.com/page/bhg-annual-upsell

Use this content:

Are You Ready To Commit To Taking Your Business To The Next Level?

Because We're In This For The Long-Haul and Dedicated To Your Success...

Save $300 By Upgrading To An Annual Membership And Pay Only $74/mth

((BUTTON))Yes, Upgrade My Plan Right Now!

*Must prepay the full year at only $898/yr!

Target Market(s)

business owners

Industry/Entity Type

Marketing

Requirements
Must have
• 768px × 1180px IS THE SIZE vertical

Use this content:

Nice to have
• Use this content:

Should not have
• Use this content:

```html
<!DOCTYPE html>
<html lang="en">
<head>
<meta charset="utf-8">
<title>Annual Membership Upsell Banner – Bright Harbor Growth Works</title>
<link rel="stylesheet" href="https://fonts.googleapis.com/css2?family=Fira+Sans+Condensed:wght@600;700&family=Source+Sans+3:wght@400&display=swap">
<style>
  :root {
    --stage-grey: #9c9c9c;
    --paper-top: #ffffff;
    --paper-bottom: #dcdad6;
    --brand-blue: #0a66c2;
    --brand-blue-deep: #0a4e9e;
    --brand-green: #8cc63f;
    --brand-green-dark: #6fae2a;
    --white: #ffffff;
    --flyer-red: #c8202a;
    --flyer-sky: #2f86c9;
  }
  * { box-sizing: border-box; margin: 0; padding: 0; }
  html, body {
    width: 1100px;
    height: 1200px;
    overflow: hidden;
    background: var(--stage-grey);
  }
  .banner {
    position: absolute;
    left: 166px;
    top: 10px;
    width: 768px;
    height: 1180px;
    overflow: hidden;
    background: linear-gradient(180deg, var(--brand-blue) 40%, var(--brand-blue-deep) 100%);
    color: var(--white);
  }
  .hero {
    position: absolute;
    inset: 0 0 auto 0;
    height: 520px;
  }
  .hero svg { display: block; }
  .flyer-stack {
    position: absolute;
    left: 75px;
    top: 25px;
    width: 595px;
    height: 420px;
    border-radius: 4px;
    background: linear-gradient(100deg, #e7e4e0 0%, #b8c9dc 35%, var(--flyer-sky) 65%, var(--flyer-red) 100%);
    opacity: 0.85;
  }
  .headline {
    position: absolute;
    left: 0;
    top: 522px;
    width: 100%;
    text-align: center;
    font-family: "Fira Sans Condensed", "Arial Narrow", sans-serif;
    font-weight: 600;
    font-size: 47px;
    line-height: 58px;
    text-transform: uppercase;
    text-shadow: 0 2px 4px rgba(0,0,0,0.35);
  }
  .headline .accent { color: var(--brand-green); }
  .subline {
    position: absolute;
    left: 0;
    top: 720px;
    width: 100%;
    text-align: center;
    font-family: "Source Sans 3", "Myriad Pro", sans-serif;
    font-size: 20.5px;
    letter-spacing: -0.2px;
  }
  .offer-frame {
    position: absolute;
    left: 45px;
    top: 779px;
    width: 694px;
    height: 263px;
  }
  .offer-text {
    position: absolute;
    left: 0;
    width: 100%;
    text-align: center;
    font-family: "Fira Sans Condensed", "Arial Narrow", sans-serif;
    font-weight: 600;
    text-transform: uppercase;
  }
  .offer-save { top: 807px; font-size: 38px; }
  .offer-detail { top: 877px; font-size: 28px; }
  .offer-price { top: 931px; font-size: 38px; }
  .cta-button {
    position: absolute;
    left: 98px;
    top: 1015px;
    width: 572px;
    height: 59px;
    border-radius: 30px;
    background: linear-gradient(180deg, #9fd45a 0%, var(--brand-green) 50%, var(--brand-green-dark) 100%);
    border: 2px solid #b9e27f;
    box-shadow: 0 2px 4px rgba(0,0,0,0.3);
    display: flex;
    align-items: center;
    justify-content: center;
    font-family: "Fira Sans Condensed", "Arial Narrow", sans-serif;
    font-weight: 700;
    font-size: 27px;
    color: var(--white);
    text-transform: uppercase;
    text-decoration: none;
    text-shadow: 0 1px 2px rgba(0,0,0,0.25);
  }
  .footnote {
    position: absolute;
    left: 0;
    top: 1103px;
    width: 100%;
    text-align: center;
    font-family: "Source Sans 3", "Myriad Pro", sans-serif;
    font-size: 23px;
  }
</style>
</head>
<body>
  <main class="banner">
    <div class="hero">
      <svg width="768" height="520" viewBox="0 0 768 520">
        <defs>
          <linearGradient id="paperFade" x1="0" y1="0" x2="0" y2="1">
            <stop offset="0" stop-color="#ffffff"/>
            <stop offset="1" stop-color="#d9d7d3"/>
          </linearGradient>
        </defs>
        <path d="M0 0 H768 V458 C680 510 560 505 430 472 C300 440 150 400 0 450 Z" fill="url(#paperFade)"/>
        <path d="M0 440 C150 395 300 432 430 465 C560 500 680 505 768 456 L768 466 C680 515 560 512 430 480 C300 448 150 410 0 460 Z" fill="var(--brand-green)"/>
      </svg>
      <div class="flyer-stack" role="img" aria-label="Fanned stack of printed travel incentive certificates featuring resort, cruise, dining and Las Vegas getaway offers"></div>
    </div>

    <h1 class="headline">
      Are You Ready To Commit To<br>
      <span class="accent">Taking Your Business</span><br>
      To The Next Level?
    </h1>

    <p class="subline">Because We're In This For The Long-Haul and Dedicated To Your Success...</p>

    <svg class="offer-frame" width="694" height="263" viewBox="0 0 694 263" aria-hidden="true">
      <path d="M1.5 169 V1.5 H692.5 V261.5 H626" fill="none" stroke="var(--white)" stroke-width="3"/>
      <path d="M1.5 244 V261.5 H55" fill="none" stroke="var(--white)" stroke-width="3"/>
    </svg>

    <p class="offer-text offer-save">Save $300</p>
    <p class="offer-text offer-detail">By Upgrading To An Annual Membership &amp;</p>
    <p class="offer-text offer-price">Pay Only $74/mth</p>

    <a class="cta-button" href="https://bhgw.pagevault-example.com/page/bhg-annual-upsell">Yes, Upgrade My Plan Right Now!</a>

    <p class="footnote">*Must prepay the full year at only $898/yr!</p>
  </main>
</body>
</html>
```